inspirational business card

I want to use the Vector on Pixmarra.com (number 61827405) and I will purchase the vector to send it to the designer once the general concept is approved. You can download it for free for a one time use on providing a design for this request.
Within the vector, insert:
Denise Halvorsen
Guidance and Cooperative

I prefer a vertical card but do not require vertical.

Contact info:

Denise Halvorsen, J.D.
Collaborative Lawyer
Certified Divorce Coach
Mediation Coach
PHONE 641/382-4076
EMAIL: dhrt@quelvo.net

Website: Guidanceandcooperative.com
Settlementcourse.com

I like greens, blue and grey. I do not want black font, and would like the font to be legible without needing perfect reading vision (no super small font).
I would like the overall theme to convey growth and nurturance.
I like the vector I selected because of the growth and light portrayed.
Not too frilly or too bold. I would like to to appeal to both sexes.

Target Market(s)

Generally professional women 35-60

Industry/Entity Type

Attorney

Font styles to use
Serif
Sans Serif

Colors
acd136
cadf82
fbf289
9d9d9d

Requirements
Must have
• My project does not need to have my photo but you could use it if you want
Nice to have
• Vertical
• I like rounded edges on the cards
Should not have
• I do not like my name appearing two times in close proximity. I'm not a flowery person.

```html
<!DOCTYPE html>
<html lang="en">
<head>
<meta charset="utf-8">
<title>Guidance and Cooperative – Business Card</title>
<link rel="stylesheet" href="https://fonts.googleapis.com/css2?family=Cinzel:wght@400&family=Source+Sans+3:wght@400&display=swap">
<style>
  :root {
    --backdrop: #e4e4e4;
    --green-deep: #4f8a3a;
    --green-mid: #5f9a3f;
    --green-text: #4e8e2f;
    --green-light: #c8df6a;
    --card-white: #ffffff;
    --card-grey: #d9d9d9;
    --white: #ffffff;
  }
  * { margin: 0; padding: 0; box-sizing: border-box; }
  html, body {
    width: 1200px; height: 554px; overflow: hidden;
    background: var(--backdrop);
  }
  .canvas { position: relative; width: 1200px; height: 554px; }
  .card {
    position: absolute; top: 122px;
    width: 532px; height: 311px;
    overflow: hidden;
  }
  /* Front */
  .card--front {
    left: 59px;
    background: radial-gradient(ellipse 70% 130% at 78% 45%, var(--card-white) 55%, var(--card-grey) 100%);
  }
  .brand {
    position: absolute; left: 18px; top: 90px; width: 246px;
    text-align: center;
  }
  .brand__circle {
    width: 84px; height: 84px; border-radius: 50%;
    margin: 0 auto 14px;
    background: radial-gradient(circle at 50% 35%, var(--green-light), var(--green-mid));
  }
  .brand__name {
    font-family: "Cinzel", serif;
    font-size: 14px; color: var(--green-text);
    letter-spacing: 0.3px; white-space: nowrap;
  }
  .details {
    position: absolute; left: 280px; top: 80px;
    font-family: "Source Sans 3", sans-serif; color: var(--green-text);
  }
  .details__name { font-size: 23px; line-height: 1.2; }
  .details__title { font-size: 13.5px; line-height: 1.35; }
  .details__titles { margin-bottom: 20px; margin-top: 4px; }
  .contact { list-style: none; }
  .contact li {
    display: flex; align-items: center;
    font-size: 14.5px; height: 25px;
  }
  .contact svg { width: 13px; height: 13px; margin-right: 10px; fill: var(--green-text); }
  /* Back */
  .card--back {
    left: 614px;
    background: linear-gradient(180deg, var(--green-light) 0%, #b4d25e 35%, var(--green-mid) 75%, var(--green-deep) 100%);
    text-align: center; color: var(--white);
  }
  .backdrop-art {
    position: absolute; left: 86px; top: 6px; width: 360px; height: 360px;
    border-radius: 50%;
    background: radial-gradient(circle, rgba(255,255,255,0.10), rgba(80,130,50,0.12) 70%, transparent 72%);
  }
  .back__circle {
    position: absolute; left: 200px; top: 60px;
    width: 132px; height: 132px; border-radius: 50%;
    background: rgba(255,255,255,0.92);
  }
  .back__name {
    position: absolute; left: 0; right: 0; top: 200px;
    font-family: "Cinzel", serif; font-size: 22px; letter-spacing: 0.5px;
  }
  .back__url {
    position: absolute; left: 0; right: 0; top: 262px;
    font-family: "Source Sans 3", sans-serif; font-size: 14px;
  }
</style>
</head>
<body>
<main class="canvas">
  <section class="card card--front">
    <div class="brand">
      <div class="brand__circle"></div>
      <p class="brand__name">Guidance and Cooperative</p>
    </div>
    <div class="details">
      <h1 class="details__name">Denise Halvorsen, J.D.</h1>
      <div class="details__titles">
        <p class="details__title">Collaborative Lawyer</p>
        <p class="details__title">Certified Divorce Coach</p>
      </div>
      <ul class="contact">
        <li><svg viewBox="0 0 16 16" aria-hidden="true"><path d="M1 5c0-2 3-3 7-3s7 1 7 3v1h-4V5H5v1H1zM4 7h8l2 6H2z"/></svg>641/382-4076</li>
        <li><svg viewBox="0 0 16 16" aria-hidden="true"><path d="M1 3h14v10H1zM2 4l6 5 6-5v1L8 10 2 5z" fill-rule="evenodd"/></svg>dhrt@quelvo.net</li>
        <li><svg viewBox="0 0 16 16" aria-hidden="true"><path d="M8 1a7 7 0 1 0 0 14A7 7 0 0 0 8 1zm0 1.3c.8.8 1.5 2.2 1.7 3.7H6.3C6.5 4.5 7.2 3.1 8 2.3zM2.4 7h3.8c0 .7 0 1.3.1 2H2.4a5.7 5.7 0 0 1 0-2zm4.9 0h1.4c.1.7.1 1.3 0 2H7.3a9 9 0 0 1 0-2zm2.5 0h3.8a5.7 5.7 0 0 1 0 2H9.8c.1-.7.1-1.3 0-2zM8 13.7c-.8-.8-1.5-2.2-1.7-3.7h3.4c-.2 1.5-.9 2.9-1.7 3.7z"/></svg>Guidanceandcooperative.com</li>
      </ul>
    </div>
  </section>

  <section class="card card--back">
    <div class="backdrop-art" role="img" aria-label="Faint soft glow behind the name"></div>
    <div class="back__circle"></div>
    <p class="back__name">Guidance and Cooperative</p>
    <p class="back__url">Guidanceandcooperative.com</p>
  </section>
</main>
</body>
</html>
```